Wine Label Logo NEW name too

We would like to see this done in more colors but, lighter ones too. the dark colors don't show up that well. Can you also do some on white wine and not just red wine?

Also, we aren't sure we will use the name Plumvelle and wonder if you could use the name Nutmeadow with the same design to see how that looks, as well?

new wine label for a brand called Plumvelle (one word) and is targeted to go after 21-40 year olds. Probably more women than men. There will be Plumvelle Red, Plumvelle White, Plumvelle Cabernet, etc. the profile of the wine will be sweet...duh!!

would love you to come up with some TAG LINE ideas, as well. Size should be between 2 1/2 to 3 inches wide and 5 to 6 inches long. Needs place holders for varietal, Cabernet. 13.5% alcohol, area wil be California. I suggest you look at a bunch of wine labels to better understand this brief.

The final design should communicate fun, sweet, wine, young, hip

Wine labels matter. Period. Now, attempting to define “fun and contemporary” is nigh on impossible, but I think it would be safe to assume that this could mean “non-traditional.” Let’s face it. Design matters to millennial consumers. Quill, Tern Lodges, Hearthline Magazine – these brands are not ONLY for millennials by any means (well, maybe Tern), but design is top priority for these brands, and these brands have top priority for millennials. Feel free to do the math. If we spend money on something, we expect it to be beautiful and often times we expect social purchases like wine to act as a public reflection of our tastes and personality. This latter expectation is no different than any other generation (if arguably more intense due to our intrinsic personal branding tendencies); however, our personalities and what we are reflecting out to our peers IS different.
Updates

What about a label that is 2 1/2 to 3 inches wide and 5-6 inches long and looks like a white or off white piece of paper that has had berries poured across it with some stains and the name Plumvelle Cabernet as the logo on the label?  Needs space for the AVA area grown to say California and the vintage 2011 and alcohol level in small letters 12.3%. 

Look at some wine labels to get a unique idea. Needs to appeal to 21-40 year old women. Needs to denote the wine is sweet

Reason: two partners are out of the country and I want them involved in the choice

Target Market(s)

Industry/Entity Type

Social

Logo Text

Plumvelle Cabernet

Logo styles of interest
Pictorial/Combination Logo
Abstract Logo
Wordmark Logo

```html
<!DOCTYPE html>
<html lang="en">
<head>
<meta charset="utf-8">
<title>Plumvelle wine label and logo variants</title>
<link rel="stylesheet" href="https://fonts.googleapis.com/css2?family=Kalam:wght@400&family=Source+Sans+3:wght@400&display=swap">
<style>
  :root {
    --bg-top: #fbfbfb;
    --bg-bottom: #d3d3d3;
    --label-top: #f9dcaa;
    --label-bottom: #fdf6e0;
    --label-edge: #1e1e1e;
    --ink: #1f1f1f;
    --red: #e8202a;
    --white-wine: #27a9e1;
    --pink: #ec1e79;
    --mark-fill: #fbe9c4;
    --script: "Kalam", cursive;
    --sans: "Source Sans 3", "Myriad Pro", sans-serif;
  }
  * { box-sizing: border-box; margin: 0; padding: 0; }
  html, body { width: 1200px; height: 900px; overflow: hidden; }
  body {
    position: relative;
    background: linear-gradient(180deg, var(--bg-top) 0%, var(--bg-bottom) 100%);
    font-family: var(--sans);
    color: var(--ink);
  }

  /* Bottle label */
  .label {
    position: absolute;
    left: 77px; top: 101px;
    width: 525px; height: 694px;
    border-top: 14px solid var(--label-edge);
    border-bottom: 14px solid var(--label-edge);
    border-radius: 10px;
    background: linear-gradient(180deg, var(--label-top) 0%, var(--label-bottom) 100%);
  }
  .label__frame {
    position: absolute;
    left: 16px; right: 16px; top: 14px; bottom: 14px;
    border: 1.5px solid var(--red);
    border-radius: 12px;
  }
  .label__vintage {
    position: absolute; left: 0; right: 0; top: 86px;
    text-align: center; font-size: 26px;
  }
  .label__region {
    position: absolute; left: 0; right: 0; top: 470px;
    text-align: center; font-family: var(--script); font-size: 31px;
  }
  .label__varietal {
    position: absolute; left: 0; right: 0; top: 532px;
    text-align: center; font-size: 27px; color: var(--red);
  }

  /* Brand lockup: name, mark beside it, variant word beneath the mark */
  .lockup { position: absolute; width: 360px; height: 156px; }
  .lockup__name {
    position: absolute; left: 0; top: 20px;
    font-family: var(--script); font-size: 62px; line-height: 1;
    color: var(--ink); white-space: nowrap;
  }
  .lockup__mark {
    position: absolute; left: 252px; top: 0;
    width: 100px; height: 100px; border-radius: 50%;
    background: var(--mark-fill);
    border: 5px solid var(--accent);
  }
  .lockup__variant {
    position: absolute; left: 190px; top: 104px;
    font-family: var(--script); font-size: 48px; line-height: 1;
    color: var(--ink); white-space: nowrap;
  }
  .lockup--red { --accent: var(--red); }
  .lockup--white { --accent: var(--white-wine); }
  .lockup--pink { --accent: var(--pink); }

  .label .lockup { left: 69px; top: 170px; }
  .variants .lockup:nth-child(1) { left: 686px; top: 120px; }
  .variants .lockup:nth-child(2) { left: 686px; top: 396px; }
  .variants .lockup:nth-child(3) { left: 686px; top: 636px; }
</style>
</head>
<body>
  <section class="label" aria-label="Plumvelle Red wine label">
    <div class="label__frame"></div>
    <p class="label__vintage">2012</p>
    <div class="lockup lockup--red">
      <span class="lockup__name">Plumvelle</span>
      <span class="lockup__mark" aria-hidden="true"></span>
      <span class="lockup__variant">Red</span>
    </div>
    <p class="label__region">Paso Robles</p>
    <p class="label__varietal">Cabernet Sauvignon</p>
  </section>

  <section class="variants" aria-label="Logo colour variants">
    <div class="lockup lockup--red">
      <span class="lockup__name">Plumvelle</span>
      <span class="lockup__mark" aria-hidden="true"></span>
      <span class="lockup__variant">Red</span>
    </div>
    <div class="lockup lockup--white">
      <span class="lockup__name">Plumvelle</span>
      <span class="lockup__mark" aria-hidden="true"></span>
      <span class="lockup__variant">White</span>
    </div>
    <div class="lockup lockup--pink">
      <span class="lockup__name">Plumvelle</span>
      <span class="lockup__mark" aria-hidden="true"></span>
      <span class="lockup__variant">Pink</span>
    </div>
  </section>
</body>
</html>
```